THE SHRIEKING AT BRAMBLEMOOR Prospectus/Deck

We need a prospectus/deck made for this Halloween event called THE SHRIEKING AT BRAMBLEMOOR. Attached is the writeup, our logo, some background photos you can use, and photos of the actual town site. For the town photos (4) could you try to make them look greyscale or smokey? I attached a sample Prospectus/Deck that was created for another event of ours to give you an idea of layout and pages.

```html
<!DOCTYPE html>
<html lang="en">
<head>
<meta charset="utf-8">
<title>The Shrieking at Bramblemoor – Prospectus</title>
<link rel="stylesheet" href="https://fonts.googleapis.com/css2?family=Roboto:wght@400;500;700&family=Creepster&display=swap">
<style>
:root{
  --canvas:#f3f3f3;
  --ink:#0a0a0a;
  --paper-text:#f1f1f1;
  --gold:#e9b546;
  --green:#6c9a3b;
  --green-deep:#4f7a2b;
  --card:rgba(112,160,62,.82);
  --title-top:#e0c23a;
  --title-bottom:#5f9a2e;
}
*{box-sizing:border-box;margin:0;padding:0}
html,body{width:1200px;height:1200px;overflow:hidden;background:var(--canvas)}
body{position:relative;font-family:"Roboto",sans-serif;color:var(--paper-text)}
.page{position:absolute;width:543px;height:387px;overflow:hidden;background:var(--ink);box-shadow:0 3px 10px rgba(0,0,0,.35)}
.page-welcome{left:39px;top:178px}
.page-about{left:619px;top:178px}
.page-vendors{left:39px;top:616px}
.page-tiers{left:620px;top:616px}
.abs{position:absolute}
.display{font-family:"Creepster",cursive;text-transform:uppercase;letter-spacing:.5px;line-height:.98;
  background:linear-gradient(180deg,var(--title-top),var(--title-bottom));-webkit-background-clip:text;background-clip:text;color:transparent}
.brand-name{font-family:"Roboto",sans-serif;font-weight:700;color:var(--green);letter-spacing:.6px;line-height:1.15}
.kicker{color:var(--gold);font-size:9px}
.body-copy{font-size:6.3px;line-height:9.4px;text-align:justify}
.page-num{width:8px;height:8px;border-radius:50%;background:var(--gold);left:525px;top:14px;font-size:5px;color:#111;text-align:center;line-height:8px;font-weight:700}
.photo{position:absolute}
/* welcome */
.welcome-photo{left:289px;top:0;width:254px;height:387px;background:radial-gradient(ellipse at 50% 45%,#4a3328 0%,#2c1c14 45%,#120c08 100%)}
/* about */
.about-photo{left:0;top:0;width:543px;height:221px;background:linear-gradient(90deg,#2a2620 0%,#4b4336 35%,#6a5a48 60%,#3a2e24 80%,#6e6a5e 100%)}
.about-shade{left:0;top:0;width:300px;height:221px;background:linear-gradient(90deg,rgba(0,0,0,.55),rgba(0,0,0,0))}
.aerial-photo{left:42px;top:240px;width:235px;height:119px;background:linear-gradient(160deg,#5d7a4a 0%,#8a8a7a 45%,#7a6a5a 60%,#6f8a5a 100%)}
.details{left:313px;top:305px;font-size:6.5px;line-height:12.5px}
.details b{color:var(--gold);font-weight:500}
/* vendors */
.street-photo{left:0;top:0;width:543px;height:387px;background:linear-gradient(180deg,#4a4a4a 0%,#3a3a3a 40%,#2e2e2e 60%,#454545 100%)}
.col-head{color:var(--gold);font-weight:700;font-size:8.5px}
.sub-head{color:var(--gold);font-size:6.5px;font-weight:500}
.vendor-list{left:17px;top:184px;list-style:none;width:270px}
.vendor-list li{display:flex;align-items:center;height:16.8px;font-size:9px}
.vendor-list li svg{width:11px;height:11px;margin-right:10px;flex:none}
.vendor-list li span{flex:1;border-bottom:.7px solid rgba(255,255,255,.45);padding-bottom:1px;margin-right:1px;max-width:211px}
/* tiers */
.field-photo{left:0;top:0;width:543px;height:387px;background:linear-gradient(180deg,#1f2a1c 0%,#37452f 40%,#26331f 70%,#141a10 100%)}
.tier{position:absolute;top:113px;width:163px;height:165px;background:var(--card);border-radius:4px}
.tier-head{height:28px;background:var(--green-deep);border-radius:4px 4px 0 0;padding:6px 0 0 30px;font-size:7.6px;line-height:9px;color:#fff}
.price{position:absolute;left:94px;top:-5px;width:59px;height:42px;background:var(--gold);color:#1a1a1a;font-weight:500;font-size:10px;line-height:12px;text-align:center;padding-top:5px;
  clip-path:polygon(0 0,100% 0,100% 82%,50% 100%,0 82%)}
.tier ul{list-style:none;padding:10px 6px 0 8px}
.tier li{font-size:6.3px;line-height:9px;padding:0 0 2.5px 6px;margin-bottom:3px;position:relative;border-bottom:.5px solid rgba(255,255,255,.3);text-align:justify}
.tier li::before{content:"";position:absolute;left:0;top:3.3px;width:2.5px;height:2.5px;border-radius:50%;background:#fff}
.tier li:last-child{border-bottom:none}
</style>
</head>
<body>

<!-- Page 1: Welcome -->
<section class="page page-welcome">
  <div class="abs brand-name" style="left:17px;top:16px;font-size:8px;width:150px">THE SHRIEKING AT<br><span style="font-size:13px">BRAMBLEMOOR</span></div>
  <div class="abs kicker" style="left:17px;top:92px">Welcome to</div>
  <h1 class="abs display" style="left:17px;top:106px;font-size:28px;width:272px">The Shrieking at Bramblemoor</h1>
  <div class="abs" style="left:17px;top:174px;color:var(--gold);font-size:12px">Where Terror Meets Hollywood Magic!</div>
  <p class="abs body-copy" style="left:17px;top:204px;width:252px">Step into our nightmare-inducing event set within a sprawling film studio lot at 1425 Concession Road 9, Ashgrove, Ontario L0K 2P0 which has been transformed into a chillingly realistic little town. As you enter, you will find yourself immersed in the eerie atmosphere of a bygone era, where each corner holds lurking horrors. Our haunted experience offers a unique opportunity for vendors to become part of the terror by occupying the shops that line the Main Street of this sinister town. From creepy curiosities to spine-chilling treats, your store front will become a focal point of fear, allowing visitors to not only scream but also shop amidst the horrors. Prepare for a spine-tingling journey like no other as you explore our haunted event in this hauntingly realistic town.</p>
  <p class="abs body-copy" style="left:17px;top:312px;width:252px">The Shrieking at Bramblemoor is an an exhilarating and spine-chilling haunted town experience that promises to deliver unforgettable thrills and scares. As we gear up for another terrifying season, we invite you to join us as a valued vendor or sponsor. This prospectus outlines the various opportunities available for your brand to be part of this highly anticipated event</p>
  <div class="photo welcome-photo" role="img" aria-label="Costumed figure in a dark robe and antlered skull mask standing in an autumn forest"></div>
</section>

<!-- Page 2: About -->
<section class="page page-about">
  <div class="photo about-photo" role="img" aria-label="Actor in a bloodied butcher costume leaning over a workbench in a dim workshop set"></div>
  <div class="abs about-shade"></div>
  <div class="abs page-num">2</div>
  <div class="abs kicker" style="left:17px;top:60px">About</div>
  <h2 class="abs display" style="left:17px;top:72px;font-size:28px;width:280px">The Shrieking at Bramblemoor</h2>
  <p class="abs body-copy" style="left:17px;top:154px;width:250px">The Shrieking at Bramblemoor is a premier haunted town attraction known for its immersive and interactive experience that pushes the boundaries of fear. Our haunted town offers a meticulously designed setting with elaborate sets, talented actors, and cutting-edge special effects to create an atmosphere of horror and suspense. We attract a diverse audience of thrill-seekers, horror enthusiasts, families, and groups of friends, ensuring a wide reach for your brand.</p>
  <div class="photo aerial-photo" role="img" aria-label="Aerial view of the small-town film lot with brick main street buildings and surrounding fields"></div>
  <h3 class="abs display" style="left:313px;top:280px;font-size:18px">Event Details:</h3>
  <div class="abs details">
    <div><b>Date:</b> October 6 – 31, 2023 (17 days)</div>
    <div><b>Location:</b> 1425 Concession Road 9, Ashgrove, Ontario L0K 2P0</div>
    <div><b>Website:</b> www.shriekingatbramblemoor.ca</div>
  </div>
</section>

<!-- Page 3: Vendor opportunities -->
<section class="page page-vendors">
  <div class="photo street-photo" role="img" aria-label="Greyscale view down the empty main street of the haunted town"></div>
  <div class="abs page-num">3</div>
  <h2 class="abs display" style="left:17px;top:64px;font-size:18px">Vendor Opportunities:</h2>
  <div class="abs col-head" style="left:17px;top:94px">ON-SITE VENDORS:</div>
  <p class="abs body-copy" style="left:17px;top:113px;width:211px">Starting at $2500 + HST (per vendor; no sharing) depending on location and type of products/services sold and offered</p>
  <p class="abs body-copy" style="left:17px;top:139px;width:211px">Set up your booth within the haunted town premises and showcase your products or services to a captive audience in one of the existing buildings. Your brand will be exposed to thousands of visitors throughout the event. Examples of suitable vendors include:</p>
  <ul class="abs vendor-list">
    <li><svg viewBox="0 0 12 12" fill="none" stroke="#ddd" stroke-width="1"><rect x="1.5" y="4" width="9" height="7"/><path d="M1 4h10L10 1.5H2z"/></svg><span>Halloween costume shops</span></li>
    <li><svg viewBox="0 0 12 12" fill="none" stroke="#ddd" stroke-width="1"><path d="M1 6l5-5h5v5l-5 5z"/><circle cx="8.5" cy="3.5" r="1"/></svg><span>Horror-themed merchandise</span></li>
    <li><svg viewBox="0 0 12 12" fill="none" stroke="#ddd" stroke-width="1"><path d="M3 1v10M1.5 1v3h3V1M8.5 1c-1.5 1-1.5 4 0 5v5"/></svg><span>Local/Artisan food vendors (pre-packaged items)</span></li>
    <li><svg viewBox="0 0 12 12" fill="none" stroke="#ddd" stroke-width="1"><path d="M2 10l6-6M8 4l2-2 1 1-2 2z"/></svg><span>Face painting and special effects makeup artists</span></li>
    <li><svg viewBox="0 0 12 12" fill="none" stroke="#ddd" stroke-width="1"><circle cx="7" cy="5" r="3.5"/><path d="M4.5 7.5L1 11"/></svg><span>Paranormal investigators or ghost tour guides</span></li>
    <li><svg viewBox="0 0 12 12" fill="none" stroke="#ddd" stroke-width="1"><rect x="1.5" y="5" width="9" height="6"/><path d="M1 3h10v2H1zM6 3v8"/></svg><span>Novelty and souvenir vendors</span></li>
    <li><svg viewBox="0 0 12 12" fill="none" stroke="#ddd" stroke-width="1"><circle cx="6" cy="5" r="4"/><path d="M3 11h6"/></svg><span>Psychic</span></li>
    <li><svg viewBox="0 0 12 12" fill="none" stroke="#ddd" stroke-width="1"><path d="M3 1h6l2 3-5 7-5-7z M1 4h10"/></svg><span>Metaphysical items and crystals</span></li>
  </ul>
  <div class="abs col-head" style="left:315px;top:94px">FOOD TRUCKS $5000 + HST max of 3-4 total</div>
  <div class="abs sub-head" style="left:315px;top:112px">Promotional Giveaways:</div>
  <p class="abs body-copy" style="left:315px;top:124px;width:211px">Partner with us to provide branded merchandise or samples to be distributed to our visitors. This opportunity allows you to directly engage with attendees and create lasting impressions of your brand.</p>
  <div class="abs sub-head" style="left:315px;top:164px">Exclusive Sponsorship:</div>
  <p class="abs body-copy" style="left:315px;top:176px;width:211px">Become an exclusive sponsor of The Shrieking at Bramblemoor. This comprehensive package offers maximum exposure and recognition for your brand. Benefits may include prominent logo placement, branding on event merchandise, on-site signage, social media promotions, and more. This option is ideal for businesses looking to establish a strong association with the haunted town and its audience.</p>
</section>

<!-- Page 4: Sponsorship tiers -->
<section class="page page-tiers">
  <div class="photo field-photo" role="img" aria-label="Stormy sky over a dark cornfield with weathered wooden crosses"></div>
  <div class="abs page-num">4</div>
  <h2 class="abs display" style="left:17px;top:50px;font-size:18px">Sponsorship Tiers:</h2>
  <p class="abs body-copy" style="left:17px;top:75px;width:250px;text-align:left">We offer different sponsorship tiers to suit your marketing goals and budget. Please note that availability is limited for each tier, and commitments will be honored on a first-come, first-served basis. The sponsorship tiers include:</p>

  <div class="tier" style="left:17px">
    <div class="tier-head">1. Platinum<br>Sponsorship:</div>
    <div class="price">$15,000 +<br>HST</div>
    <ul>
      <li>Prominent logo placement on all marketing materials, including website, posters, flyers, and social media promotions</li>
      <li>Exclusive branding on event merchandise</li>
      <li>On-site signage and banners featuring your brand</li>
      <li>Dedicated social media posts highlighting your sponsorship</li>
      <li>Recognition during event announcements and media interviews</li>
      <li>Complimentary tickets for your staff or clients</li>
    </ul>
  </div>
  <div class="tier" style="left:190px">
    <div class="tier-head">2. Gold<br>Sponsorship:</div>
    <div class="price">$10,000 +<br>HST</div>
    <ul>
      <li>Logo placement on select marketing materials, including website, posters, and social media promotions</li>
      <li>On-site signage featuring your brand</li>
      <li>Social media mentions acknowledging your sponsorship</li>
      <li>Complimentary tickets for your staff or clients</li>
    </ul>
  </div>
  <div class="tier" style="left:363px">
    <div class="tier-head">3. Silver<br>Sponsorship:</div>
    <div class="price">$5,000 +<br>HST</div>
    <ul>
      <li>Logo placement on event website and select marketing materials</li>
      <li>Exclusive branding on event merchandise</li>
      <li>On-site signage featuring your brand</li>
      <li>Complimentary tickets for your staff or clients</li>
    </ul>
  </div>

  <div class="abs body-copy" style="left:17px;top:292px;width:212px">
    <p style="margin-bottom:6px">We are open to customizing sponsorship packages to meet your specific needs and objectives.</p>
    <p style="margin-bottom:6px">If you are interested in becoming a vendor or sponsor for The Shrieking at Bramblemoor, please contact us at the following: <span style="color:var(--gold)">mara@hollowlaneevents.ca</span></p>
    <p>We would be delighted to discuss the available opportunities in more detail and tailor a package that aligns with your brand's goals.</p>
  </div>
  <div class="abs" style="left:274px;top:293px;width:.7px;height:75px;background:rgba(255,255,255,.6)"></div>
  <p class="abs body-copy" style="left:315px;top:292px;width:211px;text-align-last:right">Do not miss the chance to be part of a frightfully fantastic experience that will haunt your customers' memories for years to come. Join The Shrieking at Bramblemoor as a vendor or sponsor and make this haunted town season one to remember!</p>
  <div class="abs brand-name" style="right:17px;top:340px;font-size:6px;text-align:right">THE SHRIEKING AT<br><span style="font-size:12px">BRAMBLEMOOR</span></div>
</section>

</body>
</html>
```